Vantrel Easy to modify Email Template

I need an email template created that can be easily modified for each new email sent. What I'm trying to accomplish is a look and feel that is consistent with each email I send out. In a perfect world, I'd like a template to use as a newsletter/informational with product/service pictures and an easy way to create the text to go with it. Then I'd also like a second email that is for letting my clients know there is a promotion or sale going on. Again, something that can he easily modified. I use mail chimp and MindBody as my platform for emailing. If possible, I'd like a pop-up box or dialog box that will ask the ready to opt-in with their name and email address.
I tried to have this done last year on PixelHarbor but we could never get it to work on Mail Chimp - the black box on the attachment would never display or capture email addresses.
What was created for me last year on PixelHarbor is great with matching colors and different sections. What would be great, if possible, is to create a template where I can add different photos in the same section, different verbiage in the same section, etc.
I hope I explained it well enough.

Target Market(s)

Target market is female - 30 to 65 years old

Industry/Entity Type

Health And Wellness

Font styles to use
Serif
Other font styles liked:
• lato

Requirements
Must have
• 1) must be able to be edited (and not by a designer/programmer)
2) must have an option to capture email addresses so people can opt-in to future email campaigns
3) must have a Zen feel to it. We are a medical spa - a very relaxed office space
4) not be too busy
Nice to have
• I hope this isn't asking too much, but the email needs to be able to run on MailChimp with no glitches. I would like the template(s) to be easily modified. Maybe keep the header and footer the same, back ground the same, and just sections that can be modified. Keep the colors to match my logo and the design from last year.

```html
<!DOCTYPE html>
<html lang="en">
<head>
<meta charset="utf-8">
<title>Vantrel Medispa Newsletter</title>
<link rel="stylesheet" href="https://fonts.googleapis.com/css2?family=Lato:wght@400;700;900&display=swap">
<style>
  :root{
    --green:#6c9b2f;
    --green-light:#8dbb3c;
    --yellow:#f4e84a;
    --ink:#2b2b2b;
    --text:#3d3d3d;
    --white:#ffffff;
    --orange:#f8a400;
    --footer-top:#4a4844;
    --footer-bottom:#2e2c29;
    --paper:#f6f6f4;
  }
  *{box-sizing:border-box;margin:0;padding:0}
  html,body{width:1200px;height:3306px;overflow:hidden}
  body{font-family:"Lato",sans-serif;background:var(--paper);position:relative;color:var(--text)}
  .abs{position:absolute}

  /* header */
  .header{left:0;top:0;width:1200px;height:215px;background:var(--white)}
  .header-band{left:0;top:0;width:1200px;height:215px}
  .brand{left:34px;top:36px;display:flex;align-items:center;gap:22px}
  .brand-dot{width:132px;height:132px;border-radius:50%;border:10px solid var(--ink)}
  .brand-name{font-weight:700;font-size:64px;color:var(--ink);line-height:1}
  .social{top:50px;right:34px;display:flex;gap:14px}
  .social span{width:56px;height:56px;border-radius:50%;border:3px solid var(--white)}
  .call{top:124px;right:34px;color:var(--white);font-size:37px;font-weight:400}
  .call b{font-weight:700;font-size:42px;margin-left:12px}

  /* hero */
  .hero-photo{left:0;top:215px;width:1200px;height:800px;
    background:
      radial-gradient(ellipse 260px 330px at 340px 500px,rgba(236,232,222,.95),rgba(236,232,222,0) 75%),
      radial-gradient(ellipse 520px 220px at 300px 820px,rgba(138,124,100,.85),rgba(138,124,100,0) 80%),
      radial-gradient(ellipse 700px 300px at 900px 120px,rgba(220,208,186,.9),rgba(220,208,186,0) 80%),
      linear-gradient(180deg,#d6ccb8 0%,#cbbfa7 45%,#a8997f 80%,#8c7e68 100%)}
  .offer{left:580px;top:350px;width:584px;height:584px;border-radius:50%;background:var(--green);
    box-shadow:inset 0 0 0 8px var(--green),inset 0 0 0 11px rgba(255,255,255,.85);
    display:flex;flex-direction:column;justify-content:center;align-items:center;text-align:center;
    color:var(--white);font-weight:700;font-size:38px;line-height:53px;text-transform:uppercase}
  .offer em{font-style:normal;color:var(--yellow)}
  .hero-wave{left:0;top:900px;width:1200px;height:140px}

  /* intro */
  .intro-mark{left:46px;top:1074px;width:454px;height:370px;display:flex;align-items:center;justify-content:center}
  .intro-mark .ring{width:350px;height:350px;border-radius:50%;border:16px solid var(--ink);display:flex;align-items:center;justify-content:center}
  .intro-mark .ring span{font-weight:700;font-size:58px;color:var(--ink)}
  .intro-text{left:562px;top:1108px;width:600px;font-size:31px;line-height:50px;color:var(--text)}
  .intro-text span{display:block;white-space:nowrap}
  .intro-text .lead{display:inline;color:var(--green)}

  /* services */
  .service{width:360px;text-align:center}
  .service .badge{width:352px;height:352px;margin:0 auto;border-radius:50%;background:var(--green);
    position:relative;overflow:hidden}
  .service .photo{position:absolute;left:16px;top:16px;width:320px;height:300px;border-radius:50%}
  .service .label{margin-top:32px;font-size:28px;font-weight:700;color:var(--ink);line-height:38px;text-transform:uppercase}
  .p-facial{background:radial-gradient(circle at 35% 70%,#c8323a 0,#c8323a 14%,rgba(200,50,58,0) 40%),
    radial-gradient(circle at 75% 40%,#f0d8cc 0,rgba(240,216,204,0) 45%),linear-gradient(135deg,#8f959c,#c9ccd0)}
  .p-laser{background:radial-gradient(circle at 55% 45%,#e6b596 0,rgba(230,181,150,0) 60%),linear-gradient(135deg,#6e6258,#c48d6c 60%,#f1e6da)}
  .p-body{background:radial-gradient(circle at 50% 40%,#f1d3bd 0,rgba(241,211,189,0) 60%),linear-gradient(180deg,#e4c2a6,#f5ebe2 70%,#ffffff)}
  .p-skin{background:radial-gradient(circle at 50% 45%,#f3dccd 0,rgba(243,220,205,0) 60%),linear-gradient(90deg,#cdb49f,#f0e0d4 50%,#e9e9e9)}
  .p-products{background:radial-gradient(circle at 30% 60%,#1f49a6 0,rgba(31,73,166,0) 40%),
    radial-gradient(circle at 70% 55%,#a9b3c2 0,rgba(169,179,194,0) 40%),linear-gradient(135deg,#dfe7f5,#ffffff)}

  /* footer */
  .footer{left:0;top:2660px;width:1200px;height:646px;
    background:radial-gradient(ellipse 420px 300px at 900px 200px,rgba(110,104,96,.55),rgba(110,104,96,0) 80%),
      linear-gradient(180deg,var(--footer-top),var(--footer-bottom))}
  .footer-top{left:0;top:2640px;width:1200px;height:110px}
  .subscribe-title{left:0;top:2774px;width:1200px;text-align:center;color:var(--white);font-size:46px;font-weight:700;text-transform:uppercase}
  .subscribe-form{left:166px;top:2884px;width:924px;height:102px;border-radius:51px;background:var(--white);
    display:flex;align-items:center;padding:0 8px 0 46px}
  .subscribe-form .field{flex:1;display:flex;align-items:center;gap:18px;font-size:29px;color:#555}
  .subscribe-form .btn{width:312px;height:82px;border-radius:41px;background:var(--orange);color:var(--white);
    font-weight:700;font-size:32px;display:flex;align-items:center;justify-content:center;text-transform:uppercase}
  .more{left:0;top:3020px;width:1200px;text-align:center;color:var(--white);font-size:28px}
  .site{left:0;top:3060px;width:1200px;text-align:center;color:var(--green-light);font-size:48px}
  .footer-wave{left:0;top:3150px;width:1200px;height:156px}
  .copyright{left:0;top:3238px;width:1200px;text-align:center;color:var(--white);font-size:28px}
</style>
</head>
<body>

<header class="abs header">
  <svg class="abs header-band" viewBox="0 0 1200 215" aria-hidden="true">
    <path d="M700 0 H1200 V215 H660 C700 200 690 120 690 70 C690 30 695 10 700 0 Z" fill="var(--green)"/>
  </svg>
  <div class="abs brand">
    <div class="brand-dot"></div>
    <div class="brand-name">Vantrel</div>
  </div>
  <div class="abs social" aria-label="Social links"><span></span><span></span><span></span></div>
  <div class="abs call">Call Us:<b>240.555.0186</b></div>
</header>

<section>
  <div class="abs hero-photo" role="img" aria-label="Photo of a stack of smooth pale zen stones balanced on a rock with sand behind"></div>
  <div class="abs offer">
    <div>We are offering</div>
    <div><em>20% off on all services</em></div>
    <div>and special procedure</div>
    <div>combination deals</div>
  </div>
  <svg class="abs hero-wave" viewBox="0 0 1200 140" preserveAspectRatio="none" aria-hidden="true">
    <path d="M0 60 C300 140 800 120 1200 20 V140 H0 Z" fill="var(--paper)"/>
    <path d="M0 62 C320 120 820 110 1200 22 L1200 50 C820 130 320 140 0 80 Z" fill="var(--green)"/>
  </svg>
</section>

<section>
  <div class="abs intro-mark"><div class="ring"><span>Vantrel</span></div></div>
  <p class="abs intro-text">
    <span><span class="lead">Vantrel</span> stands for continual im-</span>
    <span>provement. Our goal is to use a variety of</span>
    <span>technologies and medical science to help</span>
    <span>our patients achieve natural beauty.</span>
    <span>Our goals are natural beauty and patient</span>
    <span>satisfactions. We strive to make sure you</span>
    <span>are happy with your look. We are commit-</span>
    <span>ted to enhance your natural beauty.</span>
  </p>
</section>

<section>
  <div class="abs service" style="left:34px;top:1654px">
    <div class="badge"><div class="photo p-facial" role="img" aria-label="Photo for facial aesthetic treatments with red rose petals"></div></div>
    <div class="label">Facial<br>Aesthetic</div>
  </div>
  <div class="abs service" style="left:428px;top:1654px">
    <div class="badge"><div class="photo p-laser" role="img" aria-label="Photo for laser treatments"></div></div>
    <div class="label">Laser<br>Treatments</div>
  </div>
  <div class="abs service" style="left:822px;top:1650px">
    <div class="badge"><div class="photo p-body" role="img" aria-label="Photo for body contouring and weight loss"></div></div>
    <div class="label">Body Contouring /<br>Weight Loss</div>
  </div>
  <div class="abs service" style="left:192px;top:2184px">
    <div class="badge"><div class="photo p-skin" role="img" aria-label="Photo for skin rejuvenation"></div></div>
    <div class="label">Skin Rejuvenation</div>
  </div>
  <div class="abs service" style="left:644px;top:2184px">
    <div class="badge"><div class="photo p-products" role="img" aria-label="Photo of blue and silver skin care product bottles with a water splash"></div></div>
    <div class="label">Skin Care Products</div>
  </div>
</section>

<footer>
  <div class="abs footer" role="img" aria-label="Soft dark background photo of a relaxing spa client"></div>
  <svg class="abs footer-top" viewBox="0 0 1200 110" preserveAspectRatio="none" aria-hidden="true">
    <path d="M0 0 H1200 V40 C800 10 400 90 0 40 Z" fill="var(--paper)"/>
    <path d="M0 40 C400 90 800 10 1200 40 L1200 70 C800 40 400 120 0 66 Z" fill="var(--green)"/>
  </svg>
  <h2 class="abs subscribe-title">Subscribe to our newsletter</h2>
  <div class="abs subscribe-form">
    <div class="field">
      <svg width="42" height="30" viewBox="0 0 42 30" aria-hidden="true">
        <rect x="0" y="0" width="42" height="30" rx="3" fill="var(--green)"/>
        <path d="M2 3 L21 17 L40 3" fill="none" stroke="var(--white)" stroke-width="3"/>
      </svg>
      <span>Your Email Address</span>
    </div>
    <div class="btn">Subscribe</div>
  </div>
  <div class="abs more">For More Information Visit</div>
  <div class="abs site">www.vantrelmedispa.com</div>
  <svg class="abs footer-wave" viewBox="0 0 1200 156" preserveAspectRatio="none" aria-hidden="true">
    <path d="M0 70 C400 10 800 20 1200 40 V156 H0 Z" fill="var(--green)"/>
    <path d="M0 62 C400 0 800 10 1200 30 L1200 42 C800 24 400 20 0 78 Z" fill="var(--white)"/>
  </svg>
  <div class="abs copyright">Copyright @ 2021 vantrelmedispa</div>
</footer>

</body>
</html>
```